Oil Field Service company needs professional business cards

Looking to clean up our current company business cards and look a little more professional. Harlow Tubular Services is a US based company that services the oil field. We deal with engineers, managers and oil rigs....................................................................................................................................................................................................................................................................................................................................................................................................

Target Market(s)

Oil and Gas professionals

Industry/Entity Type

Oil And Gas

Contact Information for Business Card

See attached photo as example

Font styles to use
Sans Serif

Colors
ec1f27

Requirements
Must have
• Company Logo, Name, Title, Cell, Office, Fax, Email.
• See attached photo
Nice to have
• External CRT, Internal CRT, Casing Crews, Torque Turn, Laydown Machine
Should not have
• Do not introduce any new pictures and keep it professional looking

```html
<!DOCTYPE html>
<html lang="en">
<head>
<meta charset="utf-8">
<title>Harlow Tubular Services — Business Cards</title>
<link rel="stylesheet" href="https://fonts.googleapis.com/css2?family=Arimo:wght@400;700&display=swap">
<style>
  :root {
    --brand-red: #ec1f27;
    --brand-red-deep: #d51a22;
    --steel: #56616b;
    --ink: #3d444b;
    --card-white: #f7f7f7;
    --backdrop: #e9e6e1;
  }
  * { box-sizing: border-box; margin: 0; padding: 0; }
  html, body {
    width: 1200px; height: 1023px; overflow: hidden;
    background: var(--backdrop);
    font-family: "Arimo", Arial, sans-serif;
  }
  .sheet { position: relative; width: 1200px; height: 1023px; }

  .card {
    position: absolute; left: 320px; width: 560px; height: 320px;
    border-radius: 18px;
    box-shadow: 0 10px 24px rgba(0,0,0,.18);
  }

  /* Front */
  .card-front {
    top: 100px;
    background: radial-gradient(circle at 50% 40%, var(--brand-red) 0%, var(--brand-red-deep) 100%);
    color: #fff;
  }
  .card-front .wordmark {
    position: absolute; top: 108px; left: 0; right: 0; text-align: center;
  }
  .wordmark-name {
    font-weight: 700; font-size: 46px; letter-spacing: 1px; line-height: 1;
  }
  .wordmark-sub {
    font-weight: 700; font-size: 15px; letter-spacing: 5px; margin-top: 8px;
  }
  .card-front .services {
    position: absolute; left: 0; right: 0; bottom: 22px; text-align: center;
    font-size: 14px; letter-spacing: .2px;
  }

  /* Back */
  .card-back {
    top: 580px;
    background: linear-gradient(135deg, #ffffff 0%, var(--card-white) 60%, #e9e9e9 100%);
    color: var(--ink);
  }
  .card-back .wordmark {
    position: absolute; top: 30px; left: 34px; color: var(--steel);
  }
  .card-back .wordmark-name { font-size: 34px; }
  .card-back .wordmark-sub { font-size: 11px; letter-spacing: 4px; margin-top: 6px; }

  .holder { position: absolute; right: 36px; bottom: 120px; text-align: right; }
  .holder-name { color: var(--brand-red); font-size: 24px; }
  .holder-title { color: var(--ink); font-size: 15px; margin-top: 4px; }

  .contacts {
    position: absolute; left: 34px; bottom: 26px; list-style: none;
    font-size: 13px; line-height: 22px;
  }
  .contacts li { display: flex; align-items: center; gap: 10px; }
  .contacts svg { width: 13px; height: 13px; fill: none; stroke: var(--brand-red); stroke-width: 1.6; }
  .contacts svg .solid { fill: var(--brand-red); stroke: none; }
</style>
</head>
<body>
<main class="sheet">

  <section class="card card-front" aria-label="Card front">
    <div class="wordmark">
      <div class="wordmark-name">HARLOW</div>
      <div class="wordmark-sub">TUBULAR SERVICES</div>
    </div>
    <p class="services">External CRT | Internal CRT | Casing Crews | Casing Crews | Laydown Machine</p>
  </section>

  <section class="card card-back" aria-label="Card back">
    <div class="wordmark">
      <div class="wordmark-name">HARLOW</div>
      <div class="wordmark-sub">TUBULAR SERVICES</div>
    </div>

    <div class="holder">
      <div class="holder-name">Your Name</div>
      <div class="holder-title">Title</div>
    </div>

    <ul class="contacts">
      <li>
        <svg viewBox="0 0 14 14"><path class="solid" d="M7 1a4 4 0 0 0-4 4c0 3 4 8 4 8s4-5 4-8a4 4 0 0 0-4-4z"/><circle cx="7" cy="5" r="1.4" fill="#fff" stroke="none"/></svg>
        Your address
      </li>
      <li>
        <svg viewBox="0 0 14 14"><circle cx="7" cy="7" r="6"/><path d="M5 4.5l1 1.6-.8.8a4 4 0 0 0 1.9 1.9l.8-.8 1.6 1-.6 1.2C6.5 10 4 7.5 3.8 5.1z" class="solid"/></svg>
        +1 555 014 1220
      </li>
      <li>
        <svg viewBox="0 0 14 14"><rect x="1.5" y="3" width="11" height="8"/><path d="M1.5 3l5.5 4.5L12.5 3"/></svg>
        johndoe@harlowtubular.com
      </li>
      <li>
        <svg viewBox="0 0 14 14"><circle cx="7" cy="7" r="5.8"/><ellipse cx="7" cy="7" rx="2.5" ry="5.8"/><path d="M1.2 7h11.6M2 4h10M2 10h10"/></svg>
        www.harlowtubular.com
      </li>
    </ul>
  </section>

</main>
</body>
</html>
```